Personal Chef Needs a Good Web Design

Hi everyone!
My name is Teo, I work as a private chef for last 10 years, traveling all around the world and cooking in private megayacht and villas.
I'm about to settle down in my hometown in Europe for a while. And therefore I need a website that will show my story, pics and recipes, nutritional advices and of course offer a Personal and Private Chef services( working for 4-5 families and bringing delicious food to their house).
My clients are extremely rich folks, but usually are down to earth ones.
I believe, the web site should be focused on attention to:
-VIP person's wife( as she is usually responsible for food for family) and be simple.
-to famous people agents and be on high level.

There will be about 10 different menus and 6 different service offers

--UPDATE--
Logo Design:
+My thoughts are- printed structure of the vegetable or fruit on a white font. Like you slice the buffalo tomato, put it in red paint and print it on the edge of the page. See attached files named logo. Can be any nice structured thing, like tomato, lemon, red cabbage etc.
+Classic logos with chef's hat or knives are good too.
+Need to have the space for me to add the name( the fonts can be provided)

Target Market(s)

Private person. 80% Russian clients.

Industry/Entity Type

Cooking

Coding

Coded - Design and coding required

Number of Pages Required

3 page

Requirements
Must have
• Contact form/ Request back call/ Schedule a free consultation
Nice to have
• The client will need to choose straight ahead from the range of services I offer, like:
• -Private Chef( cooking only for the client)
• -Personal Chef( cooking for around 5 clients, bringing the ready to be heated food to their door)
• -Romantic dinner for two
• -Professional Sommelier service
• -Build your kitchen( offering design, equipment and that will fit your requirements)
• -Other( flowers, waiters, barista, equipment rental)
• So this column should go right after the introduction/aboutme part and will lead to separate pages with how-it-works thing for each.

```html
<!DOCTYPE html>
<html lang="en">
<head>
<meta charset="utf-8">
<title>Teo Personal Chef</title>
<link href="https://fonts.googleapis.com/css2?family=Montserrat:wght@400;600;700&family=Open+Sans:wght@400;600&display=swap" rel="stylesheet">
<style>
:root{
  --gold:#c9a543;
  --gold-dark:#a8862c;
  --ink:#1b1b1b;
  --text:#555;
  --cream:#f7f3e6;
  --white:#fff;
  --footer:#111;
  --footer-bar:#262626;
}
*{box-sizing:border-box;margin:0;padding:0}
html,body{width:1200px;height:3044px;overflow:hidden}
body{font-family:"Open Sans",sans-serif;color:var(--text);background:var(--white);font-size:15px;line-height:1.6}
h1,h2,h3,h4,.brand,.nav a,.btn{font-family:"Montserrat",sans-serif}

/* hero */
.hero{position:relative;height:552px;background:linear-gradient(135deg,#3a2a1c 0%,#6b4a2e 35%,#2a1e15 70%,#4b3522 100%);color:var(--white)}
.hero::after{content:"";position:absolute;inset:0;background:rgba(0,0,0,.35)}
.hero > *{position:relative;z-index:1}
.topbar{display:flex;justify-content:space-between;align-items:center;padding:22px 60px 0 92px}
.brand{display:flex;align-items:center;gap:14px;font-weight:700;font-size:28px;line-height:1;color:var(--white)}
.brand-mark{width:70px;height:70px;border-radius:50%;background:var(--gold)}
.brand small{display:block;font-size:13px;font-weight:400;letter-spacing:1px;margin-top:4px}
.nav{display:flex;gap:42px;margin-top:-14px}
.nav a{color:var(--white);text-decoration:none;font-size:15px;padding:8px 0}
.nav a.active{color:var(--gold);border-bottom:3px solid var(--gold)}
.hero-text{text-align:center;margin-top:170px}
.hero-text h1{font-size:60px;font-weight:600;letter-spacing:4px}
.hero-text p{font-family:"Montserrat",sans-serif;font-size:34px;color:var(--gold);word-spacing:18px}
.btn{display:inline-block;background:var(--gold);color:var(--white);border:3px double var(--white);outline:2px solid var(--gold);padding:10px 26px;font-size:16px;text-decoration:none}
.hero-text .btn{margin-top:30px}
.dots{position:absolute;bottom:26px;left:0;right:0;display:flex;justify-content:center;gap:10px}
.dots span{width:12px;height:12px;border-radius:50%;border:2px solid var(--white)}
.dots span.on{background:var(--white)}

/* about */
.about{height:408px;display:flex;align-items:center;padding:0 100px 0 150px;gap:60px}
.chef-photo{width:340px;height:380px;background:linear-gradient(180deg,#f1f1f1,#cfcfcf);align-self:flex-end}
.about-copy{width:560px}
.about-copy h2{font-size:50px;color:var(--ink);line-height:1.1}
.about-copy h2 span{color:var(--gold)}
.about-copy h3{font-size:22px;color:var(--ink);font-weight:600;margin:8px 0 12px}
.about-copy p{font-size:14px}
.signature{width:120px;height:60px;margin-top:14px;background:linear-gradient(90deg,rgba(201,165,67,.35),rgba(201,165,67,.1))}

/* services */
.services{height:592px;background:var(--cream);position:relative}
.section-title{text-align:center;font-size:44px;font-weight:400;color:var(--ink);display:flex;align-items:center;justify-content:center;gap:24px}
.section-title::before,.section-title::after{content:"";width:60px;height:2px;background:var(--gold)}
.section-title em{font-style:normal;color:var(--gold)}
.services .section-title{padding-top:72px}
.services-map{position:absolute;top:0;left:0}
.hub{position:absolute;left:480px;top:210px;width:240px;height:240px;border-radius:50%;background:var(--white);border:4px solid var(--gold);padding:18px}
.hub div{width:100%;height:100%;border-radius:50%;background:radial-gradient(circle,#e4cc83,var(--gold))}
.service{position:absolute;display:flex;align-items:center;gap:14px;width:300px}
.service h4{font-size:16px;color:var(--ink);font-weight:600;line-height:1.2}
.service p{font-size:12px;line-height:1.3}
.service.left{text-align:right;flex-direction:row-reverse}
.svc-icon{flex:none;width:66px;height:66px;border-radius:50%;background:var(--ink);border:3px solid var(--gold);display:flex;align-items:center;justify-content:center}
.svc-icon i{width:26px;height:26px;border-radius:50%;border:3px solid var(--gold)}

/* recipes */
.recipes{height:608px;text-align:center;padding-top:56px}
.recipes .intro{width:880px;margin:18px auto 30px;font-size:14px}
.recipe-grid{display:flex;justify-content:center;gap:24px}
figure.recipe{flex:none;width:232px}
.recipe .pic{width:232px;height:150px;border-radius:4px}
.recipe figcaption{font-family:"Montserrat",sans-serif;font-size:18px;color:var(--ink);margin-top:16px}
.recipes .btn{margin-top:44px}

/* feature panels */
.features{height:360px;display:flex;position:relative}
.panel{flex:1;display:flex;flex-direction:column;align-items:center;padding-top:40px;color:var(--white);text-align:center}
.panel.word{background:linear-gradient(135deg,#c9a543,#8e7230)}
.panel.advice{background:linear-gradient(135deg,#3d2f1f,#5a4a2e)}
.panel-icon{width:90px;height:90px;border-radius:10px;background:rgba(0,0,0,.55)}
.panel.advice .panel-icon{border-radius:50%;background:var(--gold)}
.panel h3{font-size:28px;font-weight:400;margin:16px 0 10px;color:var(--ink)}
.panel.advice h3{color:var(--gold)}
.panel p{width:420px;font-size:13px;line-height:1.5}
.panel .btn{margin-top:26px;font-size:14px;padding:6px 16px;background:var(--ink);outline-color:var(--ink)}
.panel.advice .btn{background:var(--gold);outline-color:var(--gold)}
.features .badge{position:absolute;left:552px;top:130px;width:96px;height:96px;border-radius:50%;background:var(--white);border:4px solid var(--ink)}

/* contact */
.contact{height:320px;display:flex;padding:40px 100px 0 100px;gap:70px}
.contact-intro{width:290px}
.contact-intro h2{font-size:34px;font-weight:400;color:var(--ink);margin-bottom:16px}
.contact-intro p{font-size:13px}
.contact-form{display:grid;grid-template-columns:340px 280px;grid-template-rows:40px 40px 40px auto;gap:14px 40px;align-content:start}
.field{height:40px;border:1px solid #ccc;font-size:12px;padding:8px 10px;color:#999}
.field.message{grid-column:2;grid-row:1 / span 3;height:148px}
.contact-form .btn{grid-column:1;grid-row:4;justify-self:start;align-self:start;font-size:15px;padding:6px 16px;margin-top:6px}

/* footer */
.footer{height:152px;background:var(--footer);color:#bbb;padding:30px 100px 0;position:relative}
.footer-nav{display:flex;gap:26px;font-size:14px;color:var(--white)}
.footer-nav span{color:#666}
.footer-info{display:flex;gap:120px;margin-top:34px;font-size:13px}
.info{display:flex;gap:12px;align-items:center}
.info b{display:block;color:var(--white);font-weight:600}
.info svg{flex:none}
.footer .brand{position:absolute;right:100px;top:26px}
.footer .brand-mark{width:60px;height:60px}
.social{position:absolute;right:100px;top:110px;display:flex;gap:8px}
.social span{width:26px;height:26px;border-radius:50%;border:2px solid var(--gold)}
.copyright{height:52px;background:var(--footer-bar);color:#999;font-size:12px;padding:17px 100px}
</style>
</head>
<body>

<header class="hero">
  <div class="topbar">
    <div class="brand"><span class="brand-mark"></span><div>TEO<small>Personal Chef</small></div></div>
    <nav class="nav">
      <a class="active" href="#">Home</a><a href="#">Services</a><a href="#">Gallery</a><a href="#">Menu</a><a href="#">Contact Us</a>
    </nav>
  </div>
  <div class="hero-text">
    <h1>I AM SPECIALIST IN</h1>
    <p>Seafood · Chicken · Beef · Pork</p>
    <a class="btn" href="#">Contact Us</a>
  </div>
  <div class="dots"><span></span><span class="on"></span><span></span><span></span></div>
</header>

<section class="about">
  <div class="chef-photo" role="img" aria-label="Portrait of the chef in white uniform and hat, arms crossed"></div>
  <div class="about-copy">
    <h2><span>Teo</span> is a chef</h2>
    <h3>His Name is Teo &amp; He's A Chef,</h3>
    <p>I have cooked for private families for more than ten years, travelling the world aboard yachts and in quiet villas. Every menu starts with seasonal produce, honest technique and the tastes of the people at the table. Now settled at home, I bring the same care to a few families in the city, cooking fresh meals, planning dinners and shaping kitchens that work. Simple food, made well, served with warmth.</p>
    <div class="signature" role="img" aria-label="Chef's handwritten signature"></div>
  </div>
</section>

<section class="services">
  <h2 class="section-title"><span><em>Our</em> Services</span></h2>
  <svg class="services-map" width="1200" height="592" aria-hidden="true">
    <g stroke="#c9a543" stroke-width="1.5" fill="none">
      <path d="M420 240 L480 300 M420 330 L480 330 M420 420 L480 370"/>
      <path d="M780 240 L720 300 M780 330 L720 330 M780 420 L720 370"/>
    </g>
  </svg>
  <div class="hub"><div role="img" aria-label="Illustration of a chef carrying a dish"></div></div>

  <div class="service left" style="left:120px;top:200px"><span class="svc-icon"><i></i></span><div><h4>Private Chef</h4><p>Cooking Only For The Client</p></div></div>
  <div class="service left" style="left:120px;top:296px"><span class="svc-icon"><i></i></span><div><h4>Romantic Dinner For Two</h4><p>Cooking For Date Dinner</p></div></div>
  <div class="service left" style="left:120px;top:392px"><span class="svc-icon"><i></i></span><div><h4>Personal Chef</h4><p>Cooking For Five Clients</p></div></div>

  <div class="service" style="left:800px;top:200px"><span class="svc-icon"><i></i></span><div><h4>BUILD YOUR KITCHEN</h4><p>Design And Equipment Advice</p></div></div>
  <div class="service" style="left:800px;top:296px"><span class="svc-icon"><i></i></span><div><h4>Professional Sommelier Service</h4><p>Wine Pairing For Every Menu</p></div></div>
  <div class="service" style="left:800px;top:392px"><span class="svc-icon"><i></i></span><div><h4>OTHER</h4><p>Flowers, Waiters, Barista, Equipment Rental</p></div></div>
</section>

<section class="recipes">
  <h2 class="section-title"><span><em>New</em> Recipes</span></h2>
  <p class="intro">Fresh recipes from my kitchen, written for home cooks who want restaurant flavour without the fuss. Each dish uses seasonal ingredients, clear steps and a few chef tricks to make dinner feel special.</p>
  <div class="recipe-grid">
    <figure class="recipe"><div class="pic" role="img" aria-label="Plate of grilled shrimp" style="background:linear-gradient(135deg,#d8682f,#8c3a1c)"></div><figcaption>Seafood</figcaption></figure>
    <figure class="recipe"><div class="pic" role="img" aria-label="Roast chicken with vegetables" style="background:linear-gradient(135deg,#b9652a,#5a2f15)"></div><figcaption>Chicken</figcaption></figure>
    <figure class="recipe"><div class="pic" role="img" aria-label="Raw cuts of beef" style="background:linear-gradient(135deg,#b83a3a,#6b1e22)"></div><figcaption>Beef</figcaption></figure>
    <figure class="recipe"><div class="pic" role="img" aria-label="Grilled pork ribs" style="background:linear-gradient(135deg,#8a4a25,#3a1f12)"></div><figcaption>Pork</figcaption></figure>
  </div>
  <a class="btn" href="#">Proceed to all recipes</a>
</section>

<section class="features">
  <div class="panel word">
    <div class="panel-icon" role="img" aria-label="Dice icon"></div>
    <h3>Random Word</h3>
    <p>A short thought from the kitchen each week, about produce, travel and the small habits that make home cooking better.</p>
    <a class="btn" href="#">Read More</a>
  </div>
  <div class="panel advice">
    <div class="panel-icon" role="img" aria-label="Apple with cutlery icon"></div>
    <h3>Nutritional Advices</h3>
    <p>Balanced eating made simple: practical notes on portions, seasonal vegetables and meals that keep the whole family well.</p>
    <a class="btn" href="#">Read More</a>
  </div>
  <div class="badge" role="img" aria-label="Chef emblem"></div>
</section>

<section class="contact">
  <div class="contact-intro">
    <h2>Contact Form</h2>
    <p>Tell me about your family, your tastes and the service you need. I will call you back to plan a free consultation at a time that suits you.</p>
  </div>
  <form class="contact-form">
    <div class="field">Name</div>
    <div class="field message">Message</div>
    <div class="field">Phone</div>
    <div class="field">Email</div>
    <a class="btn" href="#">Submit</a>
  </form>
</section>

<footer class="footer">
  <div class="footer-nav">HOME <span>|</span> Services <span>|</span> Gallery <span>|</span> Menu <span>|</span> Contact Us</div>
  <div class="footer-info">
    <div class="info">
      <svg width="22" height="22" viewBox="0 0 24 24"><path fill="#c9a543" d="M12 2a7 7 0 0 0-7 7c0 5 7 13 7 13s7-8 7-13a7 7 0 0 0-7-7zm0 9.5A2.5 2.5 0 1 1 12 6.5a2.5 2.5 0 0 1 0 5z"/></svg>
      <div><b>Teo Personal Chef</b>12 Harbour Lane, Old Town</div>
    </div>
    <div class="info">
      <svg width="22" height="22" viewBox="0 0 24 24"><path fill="#c9a543" d="M6.6 10.8a15 15 0 0 0 6.6 6.6l2.2-2.2c.3-.3.7-.4 1-.2 1.1.4 2.3.6 3.6.6.6 0 1 .4 1 1V20c0 .6-.4 1-1 1A17 17 0 0 1 3 4c0-.6.4-1 1-1h3.5c.6 0 1 .4 1 1 0 1.3.2 2.5.6 3.6.1.3 0 .7-.2 1z"/></svg>
      <div><b>Call Us :</b>000-123-4567</div>
    </div>
    <div class="info">
      <svg width="22" height="22" viewBox="0 0 24 24"><path fill="#c9a543" d="M3 5h18v14H3zm2 2v.5l7 4.5 7-4.5V7l-7 4.5z"/></svg>
      <div><b>Email Us :</b>hello@teoprivatechef.com</div>
    </div>
  </div>
  <div class="brand"><span class="brand-mark"></span><div>TEO<small>Personal Chef</small></div></div>
  <div class="social"><span></span><span></span><span></span></div>
</footer>
<div class="copyright">Copyright © 2016 Teo Personal Chef. All Rights Reserved.</div>

</body>
</html>
```